Business Card Design

The Copper Lantern is a traditional English pub serving a vast range of beers and real ales. It has a very conservative oulook. Something classy would work well. We have an in-house logo. I'm thinking of good quality card in say cream with matching compliment slips and headed paper and envelopes

Industry/Entity Type

Conservative

Contact Information for Business Card

Copper Lantern Public House
58 Fenwick Row
Pinner
Middlesex
HA7 2RD
Martin D Hale - Proprietor
www.copperlanternbrook.co.uk
Tel: 020 8514 7392
Mobile; 077300 41857

Requirements
Must have
• Cl design essential. Black text.

2 sets of business cards required. one set must have my name - Martin D Hale - Proprietor and the second set should have - Louise Carver - General Manager

```html
<!DOCTYPE html>
<html lang="en">
<head>
<meta charset="utf-8">
<title>Copper Lantern Public House – Business Cards</title>
<link href="https://fonts.googleapis.com/css2?family=Open+Sans:wght@400;600;700;800&display=swap" rel="stylesheet">
<style>
  :root {
    --backdrop: #e4e1da;
    --card: #f4ecd8;
    --card-light: #f9f4e7;
    --ink: #111111;
    --ink-soft: #262626;
    --ink-muted: #4a4a4a;
    --rule: #b9ad92;
    --mark: rgba(0,0,0,0.06);
    --icon-bg: #111111;
    --icon-fg: #f4ecd8;
  }
  * { margin: 0; padding: 0; box-sizing: border-box; }
  html, body {
    width: 1200px; height: 1023px; overflow: hidden;
    background: var(--backdrop);
  }
  .icon-defs { position: absolute; width: 0; height: 0; }
  .stage {
    width: 1200px; height: 1023px;
    display: flex; flex-direction: column;
    align-items: center; justify-content: center;
    gap: 44px;
  }
  .business-card {
    position: relative;
    width: 800px; height: 440px;
    background: linear-gradient(160deg, var(--card-light) 0%, var(--card) 60%);
    border-radius: 6px;
    overflow: hidden;
    font-family: "Open Sans", Arial, sans-serif;
    color: var(--ink);
    box-shadow: 0 12px 30px rgba(0,0,0,0.16);
  }
  .brand-mark {
    position: absolute;
    left: -50px; top: 50px;
    width: 400px; height: 400px;
    border-radius: 50%;
    border: 40px solid var(--mark);
  }
  .pub-name {
    position: absolute;
    left: 300px; top: 38px;
    font-weight: 800;
    font-size: 60px;
    line-height: 1;
    letter-spacing: 1px;
    text-transform: uppercase;
  }
  .website {
    position: absolute;
    left: 303px; top: 178px;
    font-size: 17px;
    color: var(--ink-soft);
  }
  .divider {
    position: absolute;
    left: 272px; right: 36px; top: 216px;
    height: 1px;
    background: var(--rule);
  }
  .contact {
    position: absolute;
    right: 40px; top: 230px;
    text-align: right;
  }
  .contact .name {
    font-weight: 700;
    font-size: 25px;
    letter-spacing: 0.5px;
    text-transform: uppercase;
    margin-bottom: 2px;
  }
  .contact .line {
    display: flex; align-items: center; justify-content: flex-end;
    gap: 10px;
    font-size: 16px;
    line-height: 26px;
    color: var(--ink-soft);
  }
  .contact .role { padding-right: 27px; }
  .icon { width: 17px; height: 17px; flex: none; }
  .address {
    position: absolute;
    right: 40px; bottom: 22px;
    font-size: 16px;
    color: var(--ink-muted);
  }
</style>
</head>
<body>
  <svg class="icon-defs" aria-hidden="true">
    <defs>
      <symbol id="icon-phone" viewBox="0 0 18 18">
        <circle cx="9" cy="9" r="9" fill="var(--icon-bg)"/>
        <path d="M6 4.5l1.6 0 .8 2.4-1.1.9a6 6 0 0 0 2.9 2.9l.9-1.1 2.4.8 0 1.6a1.2 1.2 0 0 1-1.3 1.2A8 8 0 0 1 4.8 5.8 1.2 1.2 0 0 1 6 4.5z" fill="var(--icon-fg)"/>
      </symbol>
      <symbol id="icon-mobile" viewBox="0 0 18 18">
        <circle cx="9" cy="9" r="9" fill="var(--icon-bg)"/>
        <rect x="6" y="3.5" width="6" height="11" rx="1.2" fill="var(--icon-fg)"/>
        <rect x="7" y="5" width="4" height="6.5" fill="var(--icon-bg)"/>
      </symbol>
      <symbol id="icon-pin" viewBox="0 0 18 18">
        <circle cx="9" cy="9" r="9" fill="var(--icon-bg)"/>
        <path d="M9 3.5a3.6 3.6 0 0 0-3.6 3.6c0 2.7 3.6 7.4 3.6 7.4s3.6-4.7 3.6-7.4A3.6 3.6 0 0 0 9 3.5z" fill="var(--icon-fg)"/>
        <circle cx="9" cy="7.1" r="1.3" fill="var(--icon-bg)"/>
      </symbol>
    </defs>
  </svg>

  <main class="stage">
    <article class="business-card">
      <div class="brand-mark" aria-hidden="true"></div>
      <h1 class="pub-name">Copper<br>Lantern</h1>
      <p class="website">www.copperlanternbrook.co.uk</p>
      <div class="divider"></div>
      <section class="contact">
        <p class="name">Martin D Hale</p>
        <p class="line role">Proprietor</p>
        <p class="line">020 8514 7392 <svg class="icon" aria-hidden="true"><use href="#icon-phone"/></svg></p>
        <p class="line">077300 41857 <svg class="icon" aria-hidden="true"><use href="#icon-mobile"/></svg></p>
        <p class="line">Public House <svg class="icon" aria-hidden="true"><use href="#icon-pin"/></svg></p>
      </section>
      <p class="address">58 Fenwick Row Pinner, Middlesex HA7 2RD</p>
    </article>

    <article class="business-card">
      <div class="brand-mark" aria-hidden="true"></div>
      <h1 class="pub-name">Copper<br>Lantern</h1>
      <p class="website">www.copperlanternbrook.co.uk</p>
      <div class="divider"></div>
      <section class="contact">
        <p class="name">Louise Carver</p>
        <p class="line role">General Manager</p>
        <p class="line">020 8514 7392 <svg class="icon" aria-hidden="true"><use href="#icon-phone"/></svg></p>
        <p class="line">077300 41857 <svg class="icon" aria-hidden="true"><use href="#icon-mobile"/></svg></p>
        <p class="line">Public House <svg class="icon" aria-hidden="true"><use href="#icon-pin"/></svg></p>
      </section>
      <p class="address">58 Fenwick Row Pinner, Middlesex HA7 2RD</p>
    </article>
  </main>
</body>
</html>
```